Packaging design - allergy testing kit supplies

We provide allergy testing and treatment for veterinary clinics so we want it to be fun and scientific at the same time. We would like to limit our design to 3 colors: our PMS colors are 152, 375, and 312. The proposed packaging template is provided in the uploaded files section along with 2 versions of our logo.
We'd like the box to say these are allergy testing supplies and where the slots are will be where our marketing materials go. We'd also like it to reiterate and incorporate our brand online. Our website is www.pawsensetest.com. and would also like a place for our toll free number to be displayed as well.
Target Market(s)
US Based Veterinary clinics
Industry/Entity Type
Veterinary
Font styles to use
Other font styles liked:
- we use century gothic (bolds) and myriad pro condensed fonts
Requirements
Must have
- 3 colors:
- PMS - 152, 375 and 312
- our logo, website and space for toll free phone number
Nice to have
- a pet friendly element while still coming across scientific
- synergy with our website www.pawsensetest.com
- our fonts are: century gothic family and myriad pro (typically the condensed versions)
- simple yet sophisticated design
Should not have
- full color photographs or a color palette outside the 3 colors listed above - screens of these colors are ok.

```html
<!DOCTYPE html>
<html lang="en">
<head>
<meta charset="utf-8">
<title>Allergy Testing Kit – Packaging</title>
<link rel="stylesheet" href="https://fonts.googleapis.com/css2?family=Didact+Gothic&family=Oswald:wght@400;500&family=Roboto+Slab:wght@700&display=swap">
<style>
  :root{
    --blue:#12ADE0;
    --blue-deep:#0E9CCB;
    --green:#6BBE4E;
    --green-soft:#DDEFD3;
    --orange:#E2A233;
    --white:#FFFFFF;
    --stage:#E9EAEB;
  }
  *{margin:0;padding:0;box-sizing:border-box}
  html,body{width:1200px;height:1200px;overflow:hidden;background:var(--stage)}
  .canvas{position:relative;width:1200px;height:1200px}

  /* side panel */
  .side-panel{position:absolute;left:130px;top:90px;width:200px;height:1020px;
    background:linear-gradient(160deg,#4CC4EA 0%,var(--blue) 45%,var(--blue-deep) 100%)}
  .side-panel .web-band{position:absolute;top:0;left:0;right:0;height:70px;background:var(--blue);
    display:flex;align-items:center;justify-content:center}
  .side-panel .website{font-family:"Oswald",sans-serif;font-weight:500;font-size:19px;color:var(--white);white-space:nowrap}
  .side-panel .stripe-white{position:absolute;left:0;right:0;background:var(--white)}
  .side-panel .stripe-orange{position:absolute;left:0;right:0;background:var(--orange)}

  /* front panel */
  .front-panel{position:absolute;left:330px;top:90px;width:740px;height:1020px;background:var(--white);overflow:hidden}
  .front-panel .shapes{position:absolute;inset:0}

  .brand{position:absolute;left:60px;top:170px;display:flex;align-items:center;gap:24px}
  .brand .mark{width:54px;height:54px;background:var(--blue);flex:none}
  .brand .name{display:flex;flex-direction:column;font-family:"Didact Gothic",sans-serif;color:var(--blue);line-height:1;text-transform:uppercase;white-space:nowrap}
  .brand .name-main{font-size:64px;letter-spacing:6px}
  .brand .name-sub{font-size:40px;letter-spacing:26px;color:var(--green);margin-top:6px}

  .title-box{position:absolute;left:212px;top:395px;width:350px;height:205px;border:3px solid var(--orange);
    border-radius:6px;background:var(--white);display:flex;flex-direction:column;align-items:center;justify-content:center;gap:6px;overflow:hidden}
  .title-box span{display:block;white-space:nowrap;font-family:"Roboto Slab",serif;font-weight:700;line-height:1;transform-origin:center}
  .title-box .title-main{font-size:80px;color:var(--green);letter-spacing:-2px;transform:scaleX(.84)}
  .title-box .title-sub{font-size:54px;color:var(--blue);letter-spacing:-1px;transform:scaleX(.8)}

  .pets-illustration{position:absolute;left:0;top:640px;width:420px;height:260px;
    border-radius:48% 52% 0 0 / 60% 60% 0 0;
    background:linear-gradient(100deg,var(--blue) 0%,var(--blue) 32%,var(--orange) 45%,var(--orange) 55%,var(--green) 68%,var(--green) 100%);opacity:.9}

  .helpline{position:absolute;left:24px;bottom:18px;color:var(--white)}
  .helpline .bubble{width:100px;height:58px;border-radius:50%;border:2px solid var(--white);
    font-family:"Oswald",sans-serif;font-size:12px;line-height:1.3;display:flex;flex-direction:column;justify-content:center;padding-left:20px;margin-bottom:6px}
  .helpline .phone{font-family:"Oswald",sans-serif;font-weight:500;font-size:38px;letter-spacing:.5px;white-space:nowrap}
</style>
</head>
<body>
<div class="canvas">

  <aside class="side-panel">
    <div class="web-band"><span class="website">www.pawsensetest.com</span></div>
    <div class="stripe-white" style="top:70px;height:50px"></div>
    <div class="stripe-orange" style="top:120px;height:28px"></div>
    <div class="stripe-orange" style="top:800px;height:62px"></div>
    <div class="stripe-white" style="top:862px;height:60px"></div>
  </aside>

  <section class="front-panel">
    <svg class="shapes" width="740" height="1020" viewBox="0 0 740 1020">
      <defs>
        <linearGradient id="screen-fade" x1="0" y1="0" x2="1" y2="1">
          <stop offset="0" stop-color="var(--green-soft)"/>
          <stop offset="0.6" stop-color="#FFFFFF"/>
        </linearGradient>
      </defs>
      <path class="top-wave" d="M0,0 H740 V170 C560,175 420,40 0,40 Z" fill="var(--blue)"/>
      <path class="top-rule" d="M0,80 C380,20 540,180 740,195" fill="none" stroke="var(--orange)" stroke-width="9"/>
      <path class="screen-area" d="M0,330 C250,280 480,350 740,430 V760 H0 Z" fill="url(#screen-fade)"/>
      <path class="green-swoosh" d="M0,330 C250,280 480,350 740,430" fill="none" stroke="var(--green)" stroke-width="8" opacity=".8"/>
    </svg>

    <div class="brand">
      <span class="mark"></span>
      <span class="name"><span class="name-main">Brightpath</span><span class="name-sub">Labs</span></span>
    </div>

    <div class="title-box">
      <span class="title-main">ALLERGY</span>
      <span class="title-sub">TESTING KIT</span>
    </div>

    <div class="pets-illustration" role="img" aria-label="Line illustration of three dogs in blue, orange and green"></div>

    <svg class="shapes" width="740" height="1020" viewBox="0 0 740 1020">
      <path class="bottom-wave" d="M0,830 C220,965 500,990 740,955 V1020 H0 Z" fill="var(--blue)"/>
      <path class="bottom-rule" d="M0,805 C230,950 500,975 740,930" fill="none" stroke="var(--orange)" stroke-width="9"/>

      <g class="detail-hex" font-family="Oswald, sans-serif" fill="var(--white)">
        <polygon points="575,570 650,613 650,700 575,743 500,700 500,613" fill="var(--orange)"/>
        <text x="528" y="645" font-size="17">SOME TEXTS</text>
        <text x="528" y="665" font-size="15">FOR PRODUCT</text>
        <text x="528" y="697" font-size="27">DETAILS</text>

        <polygon points="500,735 575,778 575,865 500,908 425,865 425,778" fill="var(--blue)"/>
        <text x="453" y="810" font-size="17">SOME TEXTS</text>
        <text x="453" y="830" font-size="15">FOR PRODUCT</text>
        <text x="453" y="862" font-size="27">DETAILS</text>

        <polygon points="652,735 727,778 727,865 652,908 577,865 577,778" fill="var(--green)"/>
        <text x="605" y="810" font-size="17">SOME TEXTS</text>
        <text x="605" y="830" font-size="15">FOR PRODUCT</text>
        <text x="605" y="862" font-size="27">DETAILS</text>
      </g>
    </svg>

    <div class="helpline">
      <div class="bubble"><span>We'll be</span><span>Happy to Help</span></div>
      <div class="phone">1-800-555-0142</div>
    </div>
  </section>

</div>
</body>
</html>
```